7KQ Pop Up Shop Clearance Flyer

We sell furniture. We opened up recently a temporary pop up shop to clear some stock we had from our old shop. So we don't have a full collection just our clearance lines that we want to get rid of - but the customer doesn't need to know this! Therefore the aim of this leaflet is to attract customers and make them come in - once they are there they might see something they like. As we will not be there for long - just a few more weeks.
We need a flyer to promote locally our pop up shop (temporary shop) with a Clearance Sale. The flyer will be sent by post or by hand to the local residents and by email to ex customers that bought from us before and we have their email address...
We need a modern fresh design flyer. At the next stage we will provide text for each item (brief description, dimensions and price) so allow some space for this.
Maybe we need to add a message or something to make people want to come quickly? For example most of the items are ex display or the last item and if they want it they should hurry as one is gone its gone. or you may have a better suggestion - let me know.
if you want to see some ideas of our website then 7KQ.co.uk

Target Market(s)

Local Residents around shop

Industry/Entity Type

Retail

Colors
0255a3
3176b5
85abd2

Requirements
Must have
• price tag showing RRP or WAS price and the Clearance Sale price
• Opening Hours: Mon-Fri 9:00am - 5:00pm, Sat: 9:00am - 4:00pm, Sun: Closed
• Tel: 0208 615 2973
• Shop Address: 142 Birchwood Row, Alder Vale, London, N21 7QD
Nice to have
• Parking behind Bo Pattersons
• Map of location

```html
<!DOCTYPE html>
<html lang="en">
<head>
<meta charset="utf-8">
<title>7KQ Clearance Sale Flyer</title>
<link rel="stylesheet" href="https://fonts.googleapis.com/css2?family=Barlow:ital,wght@1,800&family=Barlow+Semi+Condensed:ital,wght@1,500&family=Lato:wght@400;700;900&display=swap">
<style>
  :root {
    --brand-blue: #0255a3;
    --mid-blue: #3176b5;
    --light-blue: #85abd2;
    --panel-blue: #0f6db5;
    --ink: #1c1c1c;
    --grey: #6d6d6d;
    --rule-grey: #8a8a8a;
    --white: #ffffff;
  }
  * { margin: 0; padding: 0; box-sizing: border-box; }
  html, body { width: 877px; height: 1200px; overflow: hidden; background: var(--white); }
  .flyer { position: relative; width: 877px; height: 1200px; overflow: hidden; background: var(--white); font-family: "Lato", sans-serif; }

  .headline {
    position: absolute; left: 52px; top: 60px;
    font-family: "Barlow", sans-serif; font-style: italic; font-weight: 800;
    font-size: 129px; line-height: 1; letter-spacing: -3px; color: var(--brand-blue);
    white-space: nowrap;
  }
  .subhead {
    position: absolute; left: 64px; top: 198px;
    font-family: "Barlow Semi Condensed", sans-serif; font-style: italic; font-weight: 500;
    font-size: 32px; line-height: 41px; color: var(--grey);
  }

  .hero-shapes { position: absolute; left: 0; top: 0; width: 877px; height: 740px; }

  .hero-price {
    position: absolute; right: 33px; top: 292px; text-align: right; color: var(--white);
  }
  .hero-price .now { font-weight: 700; font-size: 88px; line-height: 1; letter-spacing: 1px; }
  .hero-price .amount { font-weight: 700; font-size: 54px; line-height: 1; margin-top: 14px; }
  .hero-price .divider { width: 244px; height: 2px; background: var(--white); margin: 22px 0 14px auto; }
  .hero-price .old { font-weight: 900; font-size: 30px; line-height: 36px; }

  .item { position: absolute; left: 33px; width: 386px; }
  .item .photo { height: 181px; }
  .item .tag {
    height: 33px; background: var(--brand-blue); color: var(--white);
    font-weight: 700; font-size: 16px; line-height: 33px; text-align: center;
  }
  .item-lounger { top: 677px; }
  .item-lounger .photo { background: linear-gradient(160deg, #f1f0ed 0%, #dedbd5 60%, #b9aa98 100%); }
  .item-armchair { top: 927px; }
  .item-armchair .photo { background: linear-gradient(120deg, #c9b9a6 0%, #d89b3a 45%, #8c5a3a 100%); }

  .hours {
    position: absolute; left: 467px; top: 803px; width: 373px; height: 76px;
    border: 3px solid var(--mid-blue); border-top: none; border-bottom: none;
    color: var(--mid-blue); font-weight: 700; font-size: 19.5px; line-height: 25px; text-align: center;
  }
  .hours::before, .hours::after {
    content: ""; position: absolute; height: 3px; background: var(--mid-blue);
  }
  .hours::before { top: 0; left: 0; width: 100%; background: linear-gradient(to right, var(--mid-blue) 0 26%, transparent 26% 74%, var(--mid-blue) 74%); }
  .hours::after { bottom: 0; left: 0; width: 100%; background: linear-gradient(to right, var(--mid-blue) 0 28%, transparent 28% 72%, var(--mid-blue) 72%); }
  .hours .title { position: absolute; left: 0; right: 0; top: -14px; }
  .hours .lines { position: absolute; left: 0; right: 0; top: 12px; }
  .hours .closed { position: absolute; left: 0; right: 0; bottom: -12px; }

  .brand {
    position: absolute; left: 462px; top: 902px; display: flex; align-items: center; gap: 14px;
  }
  .brand .mark { width: 58px; height: 58px; background: var(--brand-blue); }
  .brand .name { font-weight: 400; font-size: 29px; line-height: 1; color: var(--ink); letter-spacing: 0.5px; }
  .brand .tagline { font-weight: 400; font-size: 13.5px; color: var(--ink); letter-spacing: 0.5px; margin-top: 6px; margin-left: 20px; }

  .contact {
    position: absolute; left: 467px; top: 1002px; width: 377px; height: 139px;
    background: var(--panel-blue); color: var(--white); text-align: center;
  }
  .contact .tel { font-weight: 900; font-size: 33px; line-height: 1; margin-top: 14px; }
  .contact .rule { width: 286px; height: 2px; background: var(--white); margin: 11px auto 9px; }
  .contact .address { font-size: 15.5px; line-height: 17.5px; }
</style>
</head>
<body>
<div class="flyer">
  <h1 class="headline">Clearance Sale</h1>
  <p class="subhead">For All Types Of Furnitures Supplied<br>From Basic To Luxury</p>

  <svg class="hero-shapes" viewBox="0 0 877 740" aria-hidden="false">
    <defs>
      <linearGradient id="navyBand" x1="0" y1="0" x2="1" y2="0">
        <stop offset="0" stop-color="#0c2559"/>
        <stop offset="1" stop-color="#1f4f9a"/>
      </linearGradient>
      <linearGradient id="blueBand" x1="0" y1="0" x2="1" y2="0">
        <stop offset="0" stop-color="#0a3b86"/>
        <stop offset="0.5" stop-color="#0255a3"/>
        <stop offset="1" stop-color="#0d47a1"/>
      </linearGradient>
      <linearGradient id="bedroomTones" x1="0" y1="0" x2="1" y2="1">
        <stop offset="0" stop-color="#e9e7e3"/>
        <stop offset="0.5" stop-color="#8a7a6a"/>
        <stop offset="1" stop-color="#c7705a"/>
      </linearGradient>
    </defs>
    <rect x="0" y="283" width="416" height="11" fill="var(--rule-grey)"/>
    <rect x="0" y="296" width="662" height="300" fill="url(#bedroomTones)" role="img" aria-label="Photo of a wooden bed with striped bedding, bedside tables and lamps"/>
    <polygon points="403,292 419,239 453,292" fill="var(--brand-blue)"/>
    <polygon points="419,239 877,239 877,596 656,596" fill="var(--ink)"/>
    <rect x="0" y="596" width="352" height="11" fill="var(--rule-grey)"/>
    <polygon points="346,598 674,598 593,685 431,685" fill="url(#navyBand)"/>
    <polygon points="660,598 877,598 877,713 593,713" fill="url(#blueBand)"/>
    <polygon points="562,687 614,687 593,713" fill="var(--ink)"/>
  </svg>

  <div class="hero-price">
    <div class="now">NOW</div>
    <div class="amount">$ 00.00</div>
    <div class="divider"></div>
    <div class="old">RRP $ 00.00</div>
    <div class="old">WAS $ 00.00</div>
  </div>

  <div class="item item-lounger">
    <div class="photo" role="img" aria-label="Photo of a modern upholstered lounger in a bright room"></div>
    <div class="tag">NOW $ 00.00 | RRP $ 00.00 | WAS $ 00.00</div>
  </div>
  <div class="item item-armchair">
    <div class="photo" role="img" aria-label="Photo of a mustard wingback armchair beside a small side table"></div>
    <div class="tag">NOW $ 00.00 | RRP $ 00.00 | WAS $ 00.00</div>
  </div>

  <div class="hours">
    <div class="title">Opening Hours:</div>
    <div class="lines">Monday to Friday: 9:00am-5:00pm<br>Saturday : 9:00am-4:00pm</div>
    <div class="closed">Sundany: Closed</div>
  </div>

  <div class="brand">
    <div class="mark"></div>
    <div>
      <div class="name">7KQ FURNITURE</div>
      <div class="tagline">TRADE FURNITURE SOLUTIONS</div>
    </div>
  </div>

  <div class="contact">
    <div class="tel">Tel: 0208 615 2973</div>
    <div class="rule"></div>
    <div class="address">Shop Address: 142 Birchwood Row,<br>Alder Vale, London, N21 7QD<br>Parking : behind Bo Pattersons</div>
  </div>
</div>
</body>
</html>
```